Up to the Challenge? Canadian based consulting company needs a two sided business card design

A Canadian based security risk management consulting company needs a two-sided business card design. What we do is provide advice and guidance related to emergency, security and business continuity management for small, medium and large companies to help ensure the protection of their people, assets, information, services, operations and reputation.

The final design should be simple, only one or two colours, eye catching, professional and one that makes people look at three or more times just because it looks so darn good.

I have include examples of business cards I like.

Target Market(s)

Small, medium and large companies.

Industry/Entity Type

Security

Contact Information for Business Card

Business Card Size: Standard size of 3.5" (89mm) x 2.0" (51mm) - (see full specifications and guides on PRINTA's website if required)
Card Stock: Looking to use PRINTA's Velda 32pt stock textured paper - seam colour either chili red or black
Business Name: The Harrowfield Group
Website: www.theharrowfieldgroup.example
Telephone: (555)214-0397
Name: Dana Forsythe
Position: Principle
e-mail: Dana.Forsythe@theharrowfieldgroup.example

Font styles to use
Serif

Colors
ec1f27
000000
9d9d9d
aaaaaa
606060

Requirements
Must have
• - "The Harrowfield Group" logo (see uploaded files). I have included grey scale and colour versions.
• - Business card details (as above)
Nice to have
• - One side black or grey scale.
• - Other side would likely be white.
• - Everyone likes the silver logo on the black background.
• - Small element of colour i.e. red but I'm leaning more to greyscale.
Should not have
• - A lot of colour. Keep it simple.

```html
<!DOCTYPE html>
<html lang="en">
<head>
<meta charset="utf-8">
<title>The Harrowfield Group – Business Card</title>
<link rel="stylesheet" href="https://fonts.googleapis.com/css2?family=PT+Serif:wght@400;700&display=swap">
<style>
  :root {
    --stage: #d9d9d9;
    --paper: #fbfbfb;
    --ink: #1a1a1a;
    --band: #606060;
    --mark-grey: #606060;
    --silver: #9d9d9d;
    --soft-grey: #aaaaaa;
    --black: #000000;
    --red: #ec1f27;
    --serif: "PT Serif", Georgia, serif;
  }
  * { box-sizing: border-box; margin: 0; padding: 0; }
  html, body {
    width: 1200px; height: 900px; overflow: hidden;
    background: var(--stage);
    font-family: var(--serif);
  }
  .stage {
    width: 1200px; height: 900px;
    display: flex; flex-direction: column;
    align-items: center; justify-content: center; gap: 40px;
  }
  .card {
    width: 700px; height: 400px; position: relative;
    box-shadow: 0 6px 18px rgba(0,0,0,.25);
    overflow: hidden;
  }

  /* Front – white */
  .card--front { background: var(--paper); color: var(--ink); }
  .brand {
    position: absolute; left: 0; right: 0; top: 52px;
    display: flex; align-items: center; justify-content: center; gap: 18px;
  }
  .brand__square { width: 34px; height: 34px; background: var(--mark-grey); }
  .brand__name {
    font-size: 34px; letter-spacing: 3px; text-transform: uppercase;
    color: var(--mark-grey); font-weight: 400;
  }
  .name-band {
    position: absolute; left: 0; right: 0; top: 168px; height: 84px;
    background: var(--band); color: #fff;
    display: flex; flex-direction: column; align-items: center; justify-content: center;
  }
  .name-band__name { font-size: 32px; letter-spacing: 1px; line-height: 1.1; }
  .name-band__title { font-size: 20px; line-height: 1.3; }
  .contacts {
    position: absolute; left: 60px; top: 278px;
    list-style: none;
    border-left: 1px solid var(--soft-grey);
    padding-left: 0;
  }
  .contacts li {
    display: flex; align-items: center; gap: 14px;
    font-size: 17px; height: 32px;
    margin-left: -10px;
  }
  .contacts svg { width: 20px; height: 20px; background: var(--paper); flex: none; }

  /* Back – black */
  .card--back { background: var(--black); }
  .back-brand {
    position: absolute; left: 0; right: 0; top: 120px;
    display: flex; align-items: center; justify-content: center; gap: 22px;
  }
  .back-brand__square { width: 44px; height: 44px; background: var(--soft-grey); }
  .back-brand__name {
    font-size: 46px; letter-spacing: 4px; text-transform: uppercase;
    color: var(--red); font-weight: 400;
  }
  .back-url {
    position: absolute; left: 0; right: 0; bottom: 58px;
    text-align: center; font-size: 22px; letter-spacing: 1px;
    color: var(--silver);
  }
</style>
</head>
<body>
<main class="stage">
  <section class="card card--front" aria-label="Card front">
    <div class="brand">
      <span class="brand__square"></span>
      <span class="brand__name">The Harrowfield Group</span>
    </div>
    <div class="name-band">
      <p class="name-band__name">Dana Forsythe</p>
      <p class="name-band__title">Principle</p>
    </div>
    <ul class="contacts">
      <li>
        <svg viewBox="0 0 20 20" aria-hidden="true"><rect x="5" y="2" width="10" height="16" rx="2" fill="none" stroke="#1a1a1a" stroke-width="1.6"/><line x1="8" y1="15" x2="12" y2="15" stroke="#1a1a1a" stroke-width="1.4"/></svg>
        (555)214-0397
      </li>
      <li>
        <svg viewBox="0 0 20 20" aria-hidden="true"><rect x="2" y="4" width="16" height="12" fill="#1a1a1a"/><path d="M2 4 L10 11 L18 4" fill="none" stroke="#fbfbfb" stroke-width="1.3"/></svg>
        Dana.Forsythe@theharrowfieldgroup.example
      </li>
      <li>
        <svg viewBox="0 0 20 20" aria-hidden="true"><circle cx="10" cy="10" r="7.5" fill="none" stroke="#1a1a1a" stroke-width="1.5"/><ellipse cx="10" cy="10" rx="3.2" ry="7.5" fill="none" stroke="#1a1a1a" stroke-width="1.2"/><line x1="2.5" y1="10" x2="17.5" y2="10" stroke="#1a1a1a" stroke-width="1.2"/></svg>
        www.theharrowfieldgroup.example
      </li>
    </ul>
  </section>

  <section class="card card--back" aria-label="Card back">
    <div class="back-brand">
      <span class="back-brand__square"></span>
      <span class="back-brand__name">The Harrowfield Group</span>
    </div>
    <p class="back-url">www.theharrowfieldgroup.example</p>
  </section>
</main>
</body>
</html>
```